Fernlymentor: an app for coaches and students in golf and fitness

I currently have an app that is called Fernlymentor and I am redoing the app completely and with this I am looking for a cool design for the app. I am not happy with the design as it is at the moment. The app should have a nice welcome and when you are logged in the dashboard must be very modern. It is a golf app that have 2 type of users. 1 user is the coach and the other user is the student. Those users can see different things of course.
The coach is normally paying a subscription charge for using the app but I want to get the students to pay for different tools that I will be offering via the app. To me the dashboard and the homepage of the app (once you have downloaded the app) is important. Here I would like to get the student as well as the coach the feeling of what the app can offer. The app offers features like Calendar (here the student can book the coach via the calendar), Chat (here the coach and the student can chat with each other as well as the coach can creat group chats with several students), Notes (here the coach as well as the student can create notes for their lessons), video tips (here the coach can upload video tips for his/her students, online lesson (the student can take online lessons by uploading recorded videos..and so on

Target Market(s)

Sport coaches (for start it will be mostly golf coaches)

Industry/Entity Type

Sports

Font styles to use
Sans Serif

Colors
0054AA
0677BA
7BADD7
CADEEF
E8F1F8

Requirements
Must have
• modern design and easy navigation.
Nice to have
• It all starts with the dashboard
Should not have
• boring standard style.

```html
<!DOCTYPE html>
<html lang="en">
<head>
<meta charset="utf-8">
<title>Fernlymentor – Notes</title>
<link href="https://fonts.googleapis.com/css2?family=Poppins:wght@400;500;600&display=swap" rel="stylesheet">
<style>
  :root{
    --brand-deep:#0054AA;
    --brand-mid:#0677BA;
    --brand-soft:#7BADD7;
    --brand-pale:#CADEEF;
    --brand-mist:#E8F1F8;
    --ink:#111827;
    --ink-soft:#4B5563;
    --ink-faint:#6B7280;
    --field:#F5F5F6;
    --card:#FFFFFF;
    --stage:#EEF4FA;
  }
  *{box-sizing:border-box;margin:0;padding:0}
  html,body{width:1200px;height:864px;overflow:hidden}
  body{background:var(--stage);font-family:"Poppins",sans-serif;position:relative}
  .phone-screen{position:absolute;left:430px;top:64px;width:340px;height:736px;border-radius:22px;overflow:hidden;background:var(--brand-deep);box-shadow:0 18px 40px rgba(0,40,90,.16)}
  .status-bar{position:absolute;left:0;right:0;top:0;height:44px;color:#fff}
  .status-time{position:absolute;left:29px;top:11px;font-size:14px;font-weight:500}
  .status-icons{position:absolute;right:14px;top:15px}
  .app-header{position:absolute;left:0;right:0;top:44px;height:40px;color:#fff;display:flex;align-items:center}
  .back-arrow{position:absolute;left:12px;top:6px}
  .header-title{position:absolute;left:40px;top:4px;font-size:15px;font-weight:500}
  .content{position:absolute;left:0;right:0;top:84px;bottom:0;background:#fff;border-radius:18px 18px 0 0}
  .search-field{position:absolute;left:18px;top:19px;width:304px;height:46px;background:var(--field);border-radius:12px;display:flex;align-items:center;padding:0 14px 0 18px;justify-content:space-between}
  .search-placeholder{font-size:12px;color:var(--ink-faint)}
  .note-card{position:absolute;width:143px;background:var(--card);border-radius:8px;box-shadow:0 2px 10px rgba(15,40,80,.10);padding:9px}
  .note-media{position:relative;height:70px;border-radius:6px;margin-bottom:10px}
  .media-fairway{background:linear-gradient(180deg,#8fc4ea 0%,#6a9a3e 45%,#4f8a2f 100%)}
  .media-clubs{background:linear-gradient(135deg,#d8c45a 0%,#8d8b5a 45%,#3a3a30 100%)}
  .media-dusk{background:linear-gradient(180deg,#b59a52 0%,#8b8a3c 50%,#5f6a2a 100%)}
  .play-button{position:absolute;left:50%;top:50%;transform:translate(-50%,-50%)}
  .note-title{font-size:12.5px;font-weight:600;color:var(--ink);margin-bottom:4px}
  .note-body{font-size:10.6px;line-height:13.6px;color:var(--ink-soft)}
  .note-footer{position:absolute;left:9px;right:9px;bottom:9px;display:flex;justify-content:space-between;align-items:center}
  .note-date{font-size:8.5px;color:var(--ink-faint)}
  .fab-add{position:absolute;left:254px;top:553px;width:68px;height:68px;border-radius:50%;background:linear-gradient(160deg,#14b8a6 0%,#1e9be8 100%);box-shadow:0 8px 18px rgba(6,119,186,.3);display:flex;align-items:center;justify-content:center}
  .home-indicator{position:absolute;left:110px;top:726px;width:120px;height:4px;border-radius:2px;background:#111}
</style>
</head>
<body>
<main class="phone-screen">
  <div class="status-bar">
    <span class="status-time">9:41</span>
    <svg class="status-icons" width="62" height="12" viewBox="0 0 62 12">
      <rect x="0" y="8" width="3" height="4" rx="1" fill="#fff"/>
      <rect x="4.5" y="6" width="3" height="6" rx="1" fill="#fff"/>
      <rect x="9" y="3.5" width="3" height="8.5" rx="1" fill="#fff"/>
      <rect x="13.5" y="1" width="3" height="11" rx="1" fill="#fff"/>
      <path d="M21 4.5a9 9 0 0 1 12 0M23.2 7a5.6 5.6 0 0 1 7.6 0" stroke="#fff" stroke-width="1.6" fill="none" stroke-linecap="round"/>
      <circle cx="27" cy="10" r="1.4" fill="#fff"/>
      <rect x="38" y="1" width="21" height="10" rx="3" stroke="#fff" stroke-opacity=".5" fill="none"/>
      <rect x="40" y="3" width="17" height="6" rx="1.5" fill="#fff"/>
      <rect x="60" y="4.5" width="1.5" height="3" rx=".7" fill="#fff" fill-opacity=".5"/>
    </svg>
  </div>
  <header class="app-header">
    <svg class="back-arrow" width="18" height="18" viewBox="0 0 18 18"><path d="M16 9H3M8 3.5 2.5 9 8 14.5" stroke="#fff" stroke-width="1.8" fill="none" stroke-linecap="round" stroke-linejoin="round"/></svg>
    <h1 class="header-title">Notes</h1>
  </header>

  <section class="content">
    <div class="search-field">
      <span class="search-placeholder">Search</span>
      <svg width="14" height="14" viewBox="0 0 14 14"><circle cx="6" cy="6" r="4.6" stroke="var(--brand-deep)" stroke-width="1.8" fill="none"/><path d="M9.5 9.5 13 13" stroke="var(--brand-deep)" stroke-width="1.8" stroke-linecap="round"/></svg>
    </div>

    <article class="note-card" style="left:18px;top:82px;height:174px">
      <div class="note-media media-fairway" role="img" aria-label="Golfer finishing a swing on the fairway">
        <svg class="play-button" width="28" height="28" viewBox="0 0 28 28"><circle cx="14" cy="14" r="14" fill="#fff"/><path d="M11 8.5v11l8.5-5.5z" stroke="#111" stroke-width="1.6" fill="none" stroke-linejoin="round"/></svg>
      </div>
      <h2 class="note-title">Sample Note</h2>
      <p class="note-body">Lorem ipsum dolor sit amet, consectetur ad...</p>
      <div class="note-footer"><span class="note-date">23 Apr at 10:16 AM</span><svg width="4" height="12"><circle cx="2" cy="2" r="1.4" fill="var(--brand-deep)"/><circle cx="2" cy="6" r="1.4" fill="var(--brand-deep)"/><circle cx="2" cy="10" r="1.4" fill="var(--brand-deep)"/></svg></div>
    </article>

    <article class="note-card" style="left:179px;top:82px;height:146px">
      <h2 class="note-title">Note Title 101</h2>
      <p class="note-body">Lorem ipsum dolor sit amet, consectetur adipiscing elit. Eu at eu eget integer aliquam blandit malesuada mauris bibendum...</p>
      <div class="note-footer"><span class="note-date">20 Apr at 8:54 PM</span><svg width="4" height="12"><circle cx="2" cy="2" r="1.4" fill="var(--brand-deep)"/><circle cx="2" cy="6" r="1.4" fill="var(--brand-deep)"/><circle cx="2" cy="10" r="1.4" fill="var(--brand-deep)"/></svg></div>
    </article>

    <article class="note-card" style="left:18px;top:272px;height:146px">
      <h2 class="note-title">Note Title 102</h2>
      <p class="note-body">Lorem ipsum dolor sit amet, consectetur adipiscing elit. Eu at eu eget integer aliquam blandit malesuada mauris bibendum...</p>
      <div class="note-footer"><span class="note-date">12 Apr at 4:38 PM</span><svg width="4" height="12"><circle cx="2" cy="2" r="1.4" fill="var(--brand-deep)"/><circle cx="2" cy="6" r="1.4" fill="var(--brand-deep)"/><circle cx="2" cy="10" r="1.4" fill="var(--brand-deep)"/></svg></div>
    </article>

    <article class="note-card" style="left:179px;top:245px;height:173px">
      <div class="note-media media-clubs" role="img" aria-label="Golf irons in a bag at sunset">
        <svg class="play-button" width="28" height="28" viewBox="0 0 28 28"><circle cx="14" cy="14" r="14" fill="#fff"/><path d="M11 8.5v11l8.5-5.5z" stroke="#111" stroke-width="1.6" fill="none" stroke-linejoin="round"/></svg>
      </div>
      <h2 class="note-title">Sample Note</h2>
      <p class="note-body">Sed vitae interdum malesuada nisi, enim...</p>
      <div class="note-footer"><span class="note-date">7 Apr at 12:46 PM</span><svg width="4" height="12"><circle cx="2" cy="2" r="1.4" fill="var(--brand-deep)"/><circle cx="2" cy="6" r="1.4" fill="var(--brand-deep)"/><circle cx="2" cy="10" r="1.4" fill="var(--brand-deep)"/></svg></div>
    </article>

    <article class="note-card" style="left:18px;top:436px;height:174px">
      <div class="note-media media-dusk" role="img" aria-label="Golf green with flag at dusk">
        <svg class="play-button" width="28" height="28" viewBox="0 0 28 28"><circle cx="14" cy="14" r="14" fill="#fff"/><path d="M11 8.5v11l8.5-5.5z" stroke="#111" stroke-width="1.6" fill="none" stroke-linejoin="round"/></svg>
      </div>
      <h2 class="note-title">Sample Note</h2>
      <p class="note-body">Lorem ipsum dolor sit amet, consectetur ad...</p>
      <div class="note-footer"><span class="note-date">7 Apr at 12:46 PM</span><svg width="4" height="12"><circle cx="2" cy="2" r="1.4" fill="var(--brand-deep)"/><circle cx="2" cy="6" r="1.4" fill="var(--brand-deep)"/><circle cx="2" cy="10" r="1.4" fill="var(--brand-deep)"/></svg></div>
    </article>

    <article class="note-card" style="left:179px;top:436px;height:164px">
      <h2 class="note-title">Note Title 102</h2>
      <p class="note-body">Ornare venenatis morbi eu fusce vitae ut suspendisse pretium integer. Auctor porttitor odio leo iaculis. Lectus velit ...</p>
      <div class="note-footer"><span class="note-date">12 Apr at 4:38 PM</span><svg width="4" height="12"><circle cx="2" cy="2" r="1.4" fill="var(--brand-deep)"/><circle cx="2" cy="6" r="1.4" fill="var(--brand-deep)"/><circle cx="2" cy="10" r="1.4" fill="var(--brand-deep)"/></svg></div>
    </article>

    <article class="note-card" style="left:18px;top:629px;height:174px">
      <div class="note-media media-fairway" role="img" aria-label="Golfer finishing a swing on the fairway">
        <svg class="play-button" width="28" height="28" viewBox="0 0 28 28"><circle cx="14" cy="14" r="14" fill="#fff"/><path d="M11 8.5v11l8.5-5.5z" stroke="#111" stroke-width="1.6" fill="none" stroke-linejoin="round"/></svg>
      </div>
    </article>

    <article class="note-card" style="left:179px;top:618px;height:146px">
      <h2 class="note-title">Note Title 102</h2>
      <p class="note-body">Lorem ipsum dolor sit amet, consectetur</p>
    </article>

    <div class="fab-add" aria-label="Add note">
      <svg width="22" height="22" viewBox="0 0 22 22"><path d="M11 2v18M2 11h18" stroke="#fff" stroke-width="2" stroke-linecap="round"/></svg>
    </div>
  </section>
  <div class="home-indicator"></div>
</main>
</body>
</html>
```